Generative AI radar Infographics

I want to create an infographic called "Automated Reasoning Horizon Chart for Tender Replies". (see slide 3 of the PowerPoint file). I want to use it on social media (Pellocast and Website). I added 2 inspiration graphics in my brief (see slide 2 of the PowerPoint). I want to add my logo on the infographic. (I also uploaded my company logos). You can find model detailed instructions on slide 1 of the PowerPoint.
Target Market(s)
Business development and sales
Industry/Entity Type
I am a business consultant. I will be using this infographics on Pellocast and in my powerpoint presentations to clients
Look and feel
Each slider illustrates characteristics of the customer's brand and the style your logo design should communicate.

```html
<!DOCTYPE html>
<html lang="en">
<head>
<meta charset="utf-8">
<title>AI Opportunity Map for Bid Response</title>
<link rel="stylesheet" href="https://fonts.googleapis.com/css2?family=Arimo:wght@400;700&family=Libre+Baskerville:wght@700&display=swap">
<style>
  :root {
    --navy: #14304a;
    --teal: #1a8ab0;
    --ink: #1c2433;
    --paper: #ffffff;
    --disc-1: #e6f2f8;
    --disc-2: #d6eaf3;
    --disc-3: #c6e1ee;
    --disc-4: #b6d8e8;
    --disc-5: #a6cfe2;
    --axis: #4d8fb0;
  }
  html, body {
    margin: 0;
    padding: 0;
    width: 1200px;
    height: 675px;
    overflow: hidden;
    background: var(--paper);
  }
  .canvas {
    width: 1200px;
    height: 675px;
    display: flex;
    align-items: center;
    justify-content: center;
  }
  .opportunity-map {
    width: 668px;
    height: 668px;
    display: block;
  }
  .title { font-family: "Libre Baskerville", Georgia, serif; font-weight: 700; font-size: 16.5px; }
  .title-main { fill: var(--navy); }
  .title-sub { fill: var(--teal); }
  .axis-label { font-family: "Arimo", Arial, sans-serif; font-weight: 700; font-size: 8.6px; fill: var(--ink); }
  .ring-label { font-family: "Libre Baskerville", Georgia, serif; font-weight: 700; font-size: 7.4px; fill: #ffffff; letter-spacing: 0.3px; }
  .item-label { font-family: "Arimo", Arial, sans-serif; font-size: 5.9px; fill: var(--ink); }
  .dot-dark { fill: var(--navy); }
  .dot-teal { fill: var(--teal); }
  .segment-dark { stroke: var(--navy); }
  .segment-teal { stroke: var(--teal); }
  .segment { fill: none; stroke-width: 19; }
  .axis-line { stroke: var(--axis); stroke-width: 0.8; }
  .axis-head { fill: var(--axis); }
  .brand-name { font-family: "Arimo", Arial, sans-serif; font-weight: 400; font-size: 6.4px; fill: var(--navy); }
</style>
</head>
<body>
<main class="canvas">
  <svg class="opportunity-map" viewBox="0 0 405 405" xmlns="http://www.w3.org/2000/svg" aria-labelledby="map-title">
    <defs>
      <path id="arc-decision" d="M 81 231 A 119 119 0 0 1 200 112"/>
      <path id="arc-development" d="M 200 112 A 119 119 0 0 1 319 231"/>
      <path id="arc-capture" d="M 73 231 A 127 127 0 0 0 200 358"/>
      <path id="arc-strategy" d="M 200 358 A 127 127 0 0 0 327 231"/>
    </defs>

    <text id="map-title" class="title title-main" x="202.5" y="30" text-anchor="middle">AI OPPORTUNITY MAP</text>
    <text class="title title-sub" x="202.5" y="54" text-anchor="middle">FOR BID RESPONSE</text>

    <text class="axis-label" x="200" y="80" text-anchor="middle">Process</text>
    <text class="axis-label" x="200" y="91" text-anchor="middle">Enhancement</text>
    <text class="axis-label" x="37" y="227" text-anchor="middle">Insights</text>
    <text class="axis-label" x="37" y="238" text-anchor="middle">Generation</text>
    <text class="axis-label" x="366" y="227" text-anchor="middle">Task</text>
    <text class="axis-label" x="366" y="238" text-anchor="middle">Automation</text>
    <text class="axis-label" x="200" y="381" text-anchor="middle">Strategy</text>
    <text class="axis-label" x="200" y="392" text-anchor="middle">Enablement</text>

    <g class="disc">
      <circle cx="200" cy="231" r="113" fill="var(--disc-1)"/>
      <circle cx="200" cy="231" r="90" fill="var(--disc-2)"/>
      <circle cx="200" cy="231" r="67" fill="var(--disc-3)"/>
      <circle cx="200" cy="231" r="44" fill="var(--disc-4)"/>
      <circle cx="200" cy="231" r="21" fill="var(--disc-5)"/>
    </g>

    <g class="ring">
      <path class="segment segment-dark" d="M 76.65 225 A 123.5 123.5 0 0 1 196 107.56"/>
      <path class="segment segment-teal" d="M 204 107.56 A 123.5 123.5 0 0 1 323.35 225"/>
      <path class="segment segment-dark" d="M 323.35 237 A 123.5 123.5 0 0 1 204 354.44"/>
      <path class="segment segment-teal" d="M 196 354.44 A 123.5 123.5 0 0 1 76.65 237"/>
      <text class="ring-label"><textPath href="#arc-decision" startOffset="50%" text-anchor="middle">DECISION SUPPORT</textPath></text>
      <text class="ring-label"><textPath href="#arc-development" startOffset="50%" text-anchor="middle">PROPOSAL DEVELOPMENT</textPath></text>
      <text class="ring-label"><textPath href="#arc-capture" startOffset="50%" text-anchor="middle">CAPTURE STRATEGY</textPath></text>
      <text class="ring-label"><textPath href="#arc-strategy" startOffset="50%" text-anchor="middle">PROPOSAL STRATEGY</textPath></text>
    </g>

    <g class="axes">
      <line class="axis-line" x1="200" y1="100" x2="200" y2="362"/>
      <line class="axis-line" x1="70" y1="231" x2="330" y2="231"/>
      <polygon class="axis-head" points="200,96 197.5,101 202.5,101"/>
      <polygon class="axis-head" points="200,366 197.5,361 202.5,361"/>
      <polygon class="axis-head" points="66,231 71,228.5 71,233.5"/>
      <polygon class="axis-head" points="334,231 329,228.5 329,233.5"/>
    </g>

    <g class="quadrant quadrant-decision">
      <circle class="dot-dark" cx="182" cy="138" r="2"/>
      <text class="item-label" x="136" y="148">Bid/No Bid Analysis</text>
      <circle class="dot-dark" cx="119" cy="158" r="2"/>
      <text class="item-label" x="124" y="160">Bid Qualification</text>
      <text class="item-label" x="113" y="172">Opportunity assessment</text>
      <circle class="dot-teal" cx="186" cy="169" r="2"/>
      <circle class="dot-dark" cx="153" cy="181" r="2"/>
      <text class="item-label" x="117" y="193">Win Probability modeling</text>
      <text class="item-label" x="101" y="204">Compliance assessment</text>
      <circle class="dot-dark" cx="175" cy="202" r="2"/>
      <circle class="dot-dark" cx="132" cy="214" r="2"/>
      <text class="item-label" x="97" y="223">Strategic Pricing optimization</text>
    </g>

    <g class="quadrant quadrant-capture">
      <text class="item-label" x="111" y="246">Customer Hot Buttons</text>
      <circle class="dot-teal" cx="178" cy="244" r="2"/>
      <circle class="dot-teal" cx="104" cy="257" r="2"/>
      <text class="item-label" x="108" y="259">SWOT Analysis</text>
      <text class="item-label" x="149" y="272">Capture Plan</text>
      <circle class="dot-teal" cx="191" cy="270" r="2"/>
      <circle class="dot-teal" cx="135" cy="278" r="2"/>
      <text class="item-label" x="116" y="288">Customer Intelligence</text>
      <circle class="dot-teal" cx="114" cy="302" r="2"/>
      <text class="item-label" x="119" y="304">Competitive Intelligence</text>
      <text class="item-label" x="133" y="319">Value Proposition</text>
      <circle class="dot-teal" cx="184" cy="317" r="2"/>
    </g>

    <g class="quadrant quadrant-development">
      <circle class="dot-teal" cx="257" cy="128" r="2"/>
      <text class="item-label" x="207" y="137">Company profile</text>
      <circle class="dot-teal" cx="208" cy="147" r="2"/>
      <text class="item-label" x="213" y="149">CV and Resumes</text>
      <text class="item-label" x="224" y="160">Past Performance</text>
      <circle class="dot-teal" cx="278" cy="158" r="2"/>
      <circle class="dot-teal" cx="243" cy="168" r="2"/>
      <text class="item-label" x="208" y="176">Due Diligence Questionnaires</text>
      <circle class="dot-teal" cx="211" cy="186" r="2"/>
      <text class="item-label" x="215" y="188">Security Questionnaires</text>
      <text class="item-label" x="248" y="197">Technical solution</text>
      <circle class="dot-teal" cx="301" cy="194" r="2"/>
      <circle class="dot-dark" cx="233" cy="208" r="2"/>
      <text class="item-label" x="237" y="209">Statement of Work</text>
      <circle class="dot-teal" cx="210" cy="216" r="2"/>
      <text class="item-label" x="214" y="218">Compliance Matrix</text>
      <circle class="dot-teal" cx="285" cy="221" r="2"/>
      <text class="item-label" x="256" y="227">Executive Summary</text>
    </g>

    <g class="quadrant quadrant-strategy">
      <circle class="dot-dark" cx="278" cy="241" r="2"/>
      <text class="item-label" x="256" y="251">Proposal outline</text>
      <circle class="dot-dark" cx="217" cy="258" r="2"/>
      <text class="item-label" x="221" y="260">Proposal plan</text>
      <circle class="dot-dark" cx="254" cy="270" r="2"/>
      <text class="item-label" x="258" y="272">Differentiators</text>
      <circle class="dot-dark" cx="262" cy="285" r="2"/>
      <text class="item-label" x="227" y="294">Win Theme extraction</text>
      <circle class="dot-dark" cx="206" cy="309" r="2"/>
      <text class="item-label" x="210" y="311">Key messages extraction</text>
    </g>

    <g class="brand">
      <text class="brand-name" x="382" y="386" text-anchor="end">Tarnwick Consulting</text>
    </g>
  </svg>
</main>
</body>
</html>
```